Letterhead design for business

Looking for an attractive and professional letterhead that uses the logo that is attached below.

Target Market(s)

Potential bankruptcy clients.

Industry/Entity Type

Legal

Colors

Designer to choose colors to be used in the design.

Requirements
Must have
• Address for locations, phone number, and website address.
• Addresses are on website ferncoveadvice.example. Use following phone number (for tracking purposes): 555-013-8274

```html
<!DOCTYPE html>
<html lang="en">
<head>
<meta charset="utf-8">
<title>Ferncove Law Group – Letterhead &amp; Folder</title>
<link href="https://fonts.googleapis.com/css2?family=Questrial&family=Lato:wght@400;700&display=swap" rel="stylesheet">
<style>
  :root{
    --backdrop:#ececec;
    --paper:#ffffff;
    --folder:#f5f5f5;
    --ink:#3a3a3a;
    --ink-dark:#111111;
    --green:#7dbb84;
    --green-band:#9dcfa2;
    --muted:#c4c4c4;
  }
  *{margin:0;padding:0;box-sizing:border-box}
  html,body{width:1200px;height:894px;overflow:hidden;background:var(--backdrop)}
  body{position:relative;font-family:'Questrial',sans-serif;color:var(--ink)}

  .letterhead{position:absolute;left:74px;top:73px;width:521px;height:674px;background:var(--paper)}
  .brand{position:absolute;display:flex;align-items:center;gap:8px;font-family:'Questrial',sans-serif;color:var(--green);white-space:nowrap}
  .brand-dot{border-radius:50%;background:var(--green)}
  .letterhead .brand--header{left:45px;top:40px;font-size:24px}
  .letterhead .brand--header .brand-dot{width:14px;height:14px}
  .website{position:absolute;right:46px;top:82px;font-family:'Lato',sans-serif;font-weight:700;font-size:9.5px;letter-spacing:3px;color:var(--ink-dark)}
  .header-rule{position:absolute;left:45px;right:46px;top:99px;border-top:1px solid var(--ink)}

  .body-copy{position:absolute;left:55px;top:132px;width:411px;font-size:11px;line-height:17.1px;text-align:justify;color:var(--ink)}
  .body-copy p+p{margin-top:17px}

  .brand--footer{left:45px;top:578px;font-size:18px;color:var(--muted)}
  .brand--footer .brand-dot{width:11px;height:11px;background:var(--muted)}
  .signature{position:absolute;right:55px;top:563px;text-align:left}
  .signature-name{font-size:14px;color:var(--ink)}
  .signature-title{font-size:9.5px;margin-top:7px;color:var(--ink)}

  .footer-rule{position:absolute;left:0;right:0;top:634px;border-top:2px solid var(--ink-dark)}
  .footer-band{position:absolute;left:0;right:0;top:636px;height:38px;background:var(--green-band);font-family:'Lato',sans-serif;text-align:center;color:#fff}
  .footer-contact{margin-top:6px;font-size:7.5px;color:var(--ink-dark)}
  .footer-contact b{font-weight:700}
  .footer-contact span+span{margin-left:9px}
  .footer-address{margin-top:4px;font-size:6px;color:#fff}
  .footer-address span+span{margin-left:10px}

  .folder{position:absolute;left:638px;top:71px;width:499px;height:677px;background:var(--folder);border-radius:16px}
  .brand--folder{left:110px;top:530px;font-size:34px}
  .brand--folder .brand-dot{width:18px;height:18px}
</style>
</head>
<body>

<section class="letterhead">
  <div class="brand brand--header"><span class="brand-dot"></span>Ferncove Law Group</div>
  <div class="website">www.ferncoveadvice.example</div>
  <div class="header-rule"></div>

  <div class="body-copy">
    <p>Lorem ipsum dolor sit amet, consectetur adipiscing elit. Donec orci purus, luctus vitae dignissim eu, iaculis sed purus. Vivamus faucibus, ipsum nec aliquet viverra, leo mauris condimentum ligula, sit amet sagittis enim ligula quis arcu. Nam egestas tortor id nisi porttitor mattis. In tortor ante, ultricies in suscipit a, tempus non massa. Vivamus et auctor mi. Fusce vel massa nulla. Phasellus nec eros mauris, et scelerisque orci. Donec malesuada orci vitae nulla accumsan porta a id massa.</p>
    <p>Quisque accumsan iaculis magna sit amet fringilla. Maecenas consequat, magna eget tincidunt semper, odio nibh rutrum mi, id feugiat ante nisi eu risus. Vestibulum nunc orci, rhoncus a placerat in, ultricies in mi. Cras mattis varius eros, vel fringilla nisi suscipit eget. Quisque scelerisque sagittis nulla at porttitor. Mauris a justo et tellus interdum tristique. Sed id augue vitae urna euismod commodo aliquet a quam. Pellentesque arcu velit, cursus et malesuada ut, consequat et diam. Nullam erat sem, rhoncus id ullamcorper vitae, rhoncus et arcu. In ultricies ultricies nulla,</p>
    <p>Kut rutrum nisi iaculis at. Donec eu magna a metus ornare faucibus. Fusce aliquet faucibus ultricies. Morbi semper, est id tincidunt gravida, sem arcu adipiscing lacus, ac bibendum nulla leo eu purus. Quisque nec diam sed risus consectetur a ccumsan quis quis nibh. Vestibulum id purus lorem. Donec eu magna a metus ornare faucibus. Fusce aliquet faucibus ultricies. Morbi semper, est id tincidunt gravida, sem arcu adipiscing lacus, ac bibendum nulla leo eu purus. Quisque nec diam sed risus consectetur a ccumsan quis quis nibh. Vestibulum id purus lorem.</p>
  </div>

  <div class="brand brand--footer"><span class="brand-dot"></span>Ferncove Law Group</div>
  <div class="signature">
    <div class="signature-name">Ellis Marrow</div>
    <div class="signature-title">Co-Founder &amp; CEO</div>
  </div>

  <div class="footer-rule"></div>
  <footer class="footer-band">
    <div class="footer-contact"><span><b>Tel:</b> 555.013.8274</span><span><b>Email:</b> info@ferncoveadvice.example</span></div>
    <div class="footer-address"><span>118 Linden Way, Oakvale, Georgia 30999</span><span>42 Harbor Ave., Suite #410 Millbrook, Georgia 30998</span></div>
  </footer>
</section>

<section class="folder">
  <div class="brand brand--folder"><span class="brand-dot"></span>Ferncove Law Group</div>
</section>

</body>
</html>
```